Linwell Psychology website transfer from WIX to Wordpress

I have a website currently coded in WIX and I want it (or something like it or better) designed to be coded on Wordpress instead. The website should have mobile optimization so that it can be viewed on mobile devices.

The current website is at: www.linwellpsychology.example

I'm not looking for versions of the website that are very different to what I already have, unless they improve on it aesthetically. I'm mainly looking to have a Wordpress version of this website that I built, away from the WIX ecosystem.
Updates

Need extra days to review

Target Market(s)

Psychology services clients

Coding

Coded - Design and coding required

Number of Pages Required

5+ page

Font styles to use
Serif

Requirements
Must have
• The finished product shoud match my website exactly.
Nice to have
• I'm happy to see new ideas that improve on the current website.
Should not have
• It should not be a different version of my website.

```html
<!DOCTYPE html>
<html lang="en">
<head>
<meta charset="utf-8">
<title>Linwell Psychology – About</title>
<link href="https://fonts.googleapis.com/css2?family=Playfair+Display:wght@400;500;600&family=Open+Sans:wght@400;600&display=swap" rel="stylesheet">
<style>
:root{
  --forest:#2f5a50;
  --forest-deep:#284a42;
  --bar:#1d2327;
  --sage:#8fb0a8;
  --white:#ffffff;
  --ink:#2f5a50;
}
*{box-sizing:border-box;margin:0;padding:0}
html,body{width:1200px;height:2250px;overflow:hidden}
body{font-family:"Playfair Display",Georgia,serif;color:var(--white);background:var(--white);position:relative}
.admin-bar{position:absolute;top:0;left:0;width:1200px;height:28px;background:var(--bar);display:flex;align-items:center;padding:0 10px;font-family:"Open Sans",Arial,sans-serif;font-size:11.5px;color:#f0f0f1;gap:16px}
.admin-bar .spacer{flex:1}
.admin-bar .dot{width:14px;height:14px;border-radius:50%;background:#a7aaad;display:inline-block;vertical-align:middle;margin-right:5px}
.site-header{position:absolute;top:28px;left:0;width:1200px;height:95px;background:var(--white)}
.brand{position:absolute;left:128px;top:30px;font-size:26px;color:var(--forest);font-weight:400}
.main-nav{position:absolute;right:128px;top:50px;display:flex;gap:23px;font-size:14px;color:var(--forest);align-items:center}
.search-icon{width:14px;height:14px}
.hero{position:absolute;top:123px;left:0;width:1200px;height:1023px;background:var(--forest)}
.portrait{position:absolute;left:138px;top:206px}
.bio{position:absolute;left:526px;top:110px;width:545px}
.bio h1{font-size:28px;font-weight:500;margin-bottom:10px}
.bio .role{font-size:14.5px;line-height:24px;font-weight:500}
.divider{display:block;margin:22px 0 30px;width:270px;height:28px}
.bio p{font-size:14px;line-height:23.8px;font-weight:500;margin-bottom:14px}
.services{position:absolute;top:1146px;left:0;width:1200px;height:432px;display:flex;justify-content:center}
.service{width:334px;text-align:center;color:var(--ink);padding-top:73px}
.service .gem{width:114px;height:112px;margin:0 auto 25px;display:block}
.service h2{font-size:23px;font-weight:400;margin-bottom:6px;letter-spacing:.2px}
.service p{font-size:14px;line-height:23.8px;letter-spacing:.3px;width:272px;margin:0 auto}
.service .more{display:block;font-size:14px;margin-top:2px;letter-spacing:.4px}
.site-footer{position:absolute;top:1578px;left:0;width:1200px;height:620px;background:var(--forest)}
.footer-col{position:absolute;font-size:14px;line-height:23.8px;font-weight:500}
.welcome{left:126px;top:70px;width:285px}
.flags{display:flex;gap:7px;position:absolute}
.flags .flag{width:137px;height:103px}
.footer-center{left:460px;top:60px;width:280px;text-align:center}
.footer-brand{height:75px;border:1px solid rgba(255,255,255,.06);display:flex;align-items:center;justify-content:center;font-size:24px;margin-bottom:58px}
.footer-center h3{font-size:16px;font-weight:500;line-height:22px}
.footer-center .note{font-size:11.5px;line-height:16px;margin-bottom:8px}
.footer-center .gap{height:26px}
.acknowledgement{left:793px;top:70px;width:283px}
.bottom-bar{position:absolute;top:2198px;left:0;width:1200px;height:52px;background:var(--forest-deep);display:flex;align-items:center;justify-content:space-between;padding:0 126px;font-size:14px;font-weight:500}
.social{display:flex;gap:18px;font-size:12px}
</style>
</head>
<body>

<div class="admin-bar">
  <span><span class="dot"></span>My Blog</span>
  <span>4</span>
  <span>0</span>
  <span>+ New</span>
  <span>Edit Page</span>
  <span><span class="dot"></span>Enable Visual Builder</span>
  <span class="spacer"></span>
  <span>Howdy, admin</span>
</div>

<header class="site-header">
  <div class="brand">Linwell Psychology</div>
  <nav class="main-nav">
    <span>Home</span><span>FAQ</span><span>About</span><span>Services</span><span>Fees &amp; Rebates</span><span>Contact</span>
    <svg class="search-icon" viewBox="0 0 14 14"><circle cx="8" cy="6" r="4.5" fill="none" stroke="#2f5a50" stroke-width="1.5"/><line x1="4.8" y1="9.2" x2="1" y2="13" stroke="#2f5a50" stroke-width="1.5"/></svg>
  </nav>
</header>

<section class="hero">
  <svg class="portrait" width="318" height="576" viewBox="0 0 318 576" role="img" aria-label="Portrait photo of the psychologist seated in an armchair writing notes">
    <defs>
      <linearGradient id="photoTone" x1="0" y1="0" x2="1" y2="1">
        <stop offset="0" stop-color="#e9e6e1"/>
        <stop offset=".5" stop-color="#8a5a44"/>
        <stop offset="1" stop-color="#5e4a3c"/>
      </linearGradient>
    </defs>
    <path d="M150 0 C250 0 318 70 316 170 C314 270 300 330 300 400 C300 500 240 560 150 574 C70 585 10 560 10 470 C10 380 0 300 0 210 C0 90 60 0 150 0Z" fill="url(#photoTone)"/>
  </svg>

  <div class="bio">
    <h1>Dr Tomas Linwell</h1>
    <div class="role">Clinical and Counselling Psychologist<br>Clinical Psychosexual Therapist</div>
    <svg class="divider" viewBox="0 0 270 28" role="img" aria-label="Decorative leaf vine divider"><rect x="0" y="12" width="270" height="4" rx="2" fill="#8fb0a8" opacity=".6"/></svg>
    <p>My name is Tomas (he/they) and I am a Clinical and Counselling Psychologist, and accredited Clinical Psychosexual Therapist, with over 15 years’ experience working with adults and young people of all abilities and identities.</p>
    <p>My practice focuses on sex therapy and working with diversity, which regularly includes supporting members of LGBTQIA+, neurodivergent, and disabled communities. Because of this work, I am sex-positive and kink-, polyamory-, LGBTQIA+ and neurodiversity knowledgeable and affirming in my practice. I am also a member of many lived experience communities as part of my commitment to lifelong learning and honoring lived experience.</p>
    <p>I know that seeing a therapist can sometimes be anxiety-evoking, and as such, I always aim to curate a non-judgmental, collaborative, and intentional approach to working with people toward their personal goals and a life of value.</p>
    <p>In my work, I balance supportive counselling with evidence-based therapies, such as: humanistic therapy, cognitive-behavioural therapy, acceptance and commitment therapy, compassion-focused therapy, and solution-focused counselling. My work is also underpinned by intersectional feminist and social justice frameworks. As part of ensuring that you are benefiting from your sessions, I will regularly check in to see if you’re finding your session helpful to ensure you feel understood, respected, and that your sessions are relevant and on track.</p>
    <p>In addition to my client work, I am also a board accredited STAP supervisor and enjoy supporting and supervising the practice of other clinicians, both trainee and experienced. And enjoy consultancy and training work with practices and organisations.</p>
  </div>
</section>

<section class="services">
  <div class="service">
    <svg class="gem" viewBox="0 0 114 112" role="img" aria-label="Line illustration of a faceted crystal"><rect width="114" height="112" rx="20" fill="#8fb0a8" opacity=".35"/></svg>
    <h2>Psychological Therapy</h2>
    <p>Psychological assessment, education, counselling, and therapy using person-centered and evidence-based integrative therapeutic interventions.</p>
    <span class="more">Learn More</span>
  </div>
  <div class="service">
    <svg class="gem" viewBox="0 0 114 112" role="img" aria-label="Line illustration of a faceted crystal"><rect width="114" height="112" rx="20" fill="#8fb0a8" opacity=".35"/></svg>
    <h2>Clinical Supervision</h2>
    <p>Clinical supervision to support provisional psychologists and registrars, early career mentoring, technical skill building, and clinical case discussion.</p>
    <span class="more">Learn More</span>
  </div>
  <div class="service">
    <svg class="gem" viewBox="0 0 114 112" role="img" aria-label="Line illustration of a faceted crystal"><rect width="114" height="112" rx="20" fill="#8fb0a8" opacity=".35"/></svg>
    <h2>Training and Consultancy</h2>
    <p>Training for general psychology or special interest subjects like sexology and neurodivergence, and consultancy for practices and organisations.</p>
    <span class="more">Learn More</span>
  </div>
</section>

<footer class="site-footer">
  <div class="footer-col welcome">
    hology, we welcome people of all backgrounds, race, ethnicity, genders, sexuality, relationship type, neurotype, and abilities. Please contact us if we can assist you to make your appointment more inclusive in any way or provide us feedback on how we can do better.
  </div>
  <div class="flags" style="left:126px;top:277px">
    <svg class="flag" viewBox="0 0 137 103" role="img" aria-label="Neurodiversity pride flag"><defs><linearGradient id="ndFlag" x1="0" y1="0" x2="0" y2="1"><stop offset="0" stop-color="#e0404a"/><stop offset=".5" stop-color="#f8c15a"/><stop offset="1" stop-color="#7fcf6a"/></linearGradient></defs><rect width="137" height="103" fill="url(#ndFlag)"/></svg>
    <svg class="flag" viewBox="0 0 137 103" role="img" aria-label="Disability pride flag"><defs><linearGradient id="dpFlag" x1="0" y1="0" x2="1" y2="1"><stop offset="0" stop-color="#595959"/><stop offset=".5" stop-color="#c9c8a8"/><stop offset="1" stop-color="#595959"/></linearGradient></defs><rect width="137" height="103" fill="url(#dpFlag)"/></svg>
  </div>

  <div class="footer-col footer-center">
    <div class="footer-brand">Linwell Psychology</div>
    <h3>Practice Hours</h3>
    <div class="note">(by appointment only):</div>
    <div>Tuesdays 10:00am – 4:00pm<br>Fridays: 9:00am – 1:30pm</div>
    <div class="gap"></div>
    <div>If you need support between appointments or after hours, please consider contacting:</div>
    <div style="height:14px"></div>
    <div>Hopeline on 13 40 20<br>Youth Talkline on 1800 402 118<br>Menscare Line on 1300 402 611<br>Night Call Back on 1300 402 733<br>Brightway on 1300 40 28 19<br>Youthspace on 1800 402 944<br>Rainbowline on 1800 402 355<br>13CIRCLE on 13 40 81</div>
  </div>

  <div class="footer-col acknowledgement">
    We acknowledge the Traditional Custodians of the lands upon which we work here in this region, the local Traditional Owners, as the first inhabitants of our nation. We recognise their continuing connection to land, water, and culture and pay our respects to their Elders past, present, and emerging – as well as First Nations people and the stolen generation who have yet to find their home. Their lands never ceded sovereignty. Always was, always will be, Aboriginal land.
  </div>
  <div class="flags" style="left:793px;top:397px;gap:2px">
    <svg class="flag" viewBox="0 0 139 93" style="width:139px;height:93px" role="img" aria-label="Aboriginal flag"><defs><linearGradient id="abFlag" x1="0" y1="0" x2="0" y2="1"><stop offset=".5" stop-color="#111"/><stop offset=".5" stop-color="#e0100f"/></linearGradient></defs><rect width="139" height="93" fill="url(#abFlag)"/></svg>
    <svg class="flag" viewBox="0 0 139 93" style="width:139px;height:93px" role="img" aria-label="Torres Strait Islander flag"><defs><linearGradient id="tsFlag" x1="0" y1="0" x2="0" y2="1"><stop offset=".15" stop-color="#0b9a6d"/><stop offset=".2" stop-color="#1a1aa8"/><stop offset=".8" stop-color="#1a1aa8"/><stop offset=".85" stop-color="#0b9a6d"/></linearGradient></defs><rect width="139" height="93" fill="url(#tsFlag)"/></svg>
  </div>
</footer>

<div class="bottom-bar">
  <span>Copyright © 2024 Linwell Psychology.</span>
  <div class="social"><span>Friendbook</span><span>Snapgram</span></div>
</div>

</body>
</html>
```